UI design needed for a prototype based on wireframe

Hey there.
I need a UI design done on a a prototype application idea before I send it to a programmer. Once designed and programmed the app will move onto a testing faze where it will stay for some time and, I assume, go through several redesign fazes. I have a wireframe mockup and background description so I imagine the design work is pretty straight forward. The app is an activity app that let´s users post different activities that they want to to and post it before a community of users who might be willing to participate. Any features worth mentioning might include Mingleport only log-in, Vantoro routes navigation and star rating system of the user. Besides that I think it´s fairly basic. This app will initially be launched only in vantoro stall because of the test feature of the marketplace.

```html
<!DOCTYPE html>
<html lang="en">
<head>
<meta charset="utf-8">
<title>Activities – Settings Menu</title>
<link href="https://fonts.googleapis.com/css2?family=Roboto:wght@400;500;700&display=swap" rel="stylesheet">
<style>
:root{
  --drawer:#263238;
  --drawer-line:#33434b;
  --appbar:#2c3b43;
  --teal:#1aa8b8;
  --white:#ffffff;
  --feed:#e6e8e9;
  --ink:#263238;
  --muted:#8a9499;
  --yellow:#f2b705;
  --red:#e53935;
  --status:#1e292e;
}
*{box-sizing:border-box;margin:0;padding:0}
html,body{width:675px;height:1200px;overflow:hidden;background:var(--white)}
body{font-family:'Roboto',Arial,sans-serif;position:relative}
.abs{position:absolute}
.status-bar{left:0;top:0;width:675px;height:45px;background:var(--status);color:var(--white);font-size:24px;display:flex;align-items:center;justify-content:flex-end;gap:14px;padding-right:22px}
.app-screen{left:490px;top:45px;width:185px;height:668px;background:var(--feed);overflow:hidden}
.app-bar{left:0;top:0;width:185px;height:205px;background:var(--appbar)}
.app-title{left:140px;top:30px;color:var(--white);font-size:44px;font-weight:500;white-space:nowrap}
.tab-label{left:95px;top:138px;color:var(--teal);font-size:29px;font-weight:500;letter-spacing:1px;white-space:nowrap}
.tab-line{left:60px;top:196px;width:125px;height:6px;background:var(--teal)}
.card{left:23px;width:200px;background:var(--white);box-shadow:0 2px 4px rgba(0,0,0,.18)}
.card .tag{position:absolute;left:22px;font-size:16px;font-weight:700}
.card .title{position:absolute;left:22px;font-size:33px;color:var(--ink);white-space:nowrap}
.card .label{position:absolute;left:34px;font-size:14px;color:var(--muted);letter-spacing:.5px}
.card .value{position:absolute;left:34px;font-size:24px;color:var(--ink)}
.card .rule{position:absolute;left:22px;width:2px;background:#dde1e3}
.card .divider{position:absolute;left:0;width:200px;height:2px;background:#eceff0}
.drawer{left:0;top:45px;width:490px;height:668px;background:var(--drawer)}
.menu-item{left:0;width:490px;height:136px;display:flex;align-items:center;gap:28px;padding-left:42px;color:var(--teal);font-size:29px;border-bottom:2px solid var(--drawer-line)}
.menu-item svg{width:34px;height:34px;fill:var(--teal)}
.logout-ring{left:300px;top:438px;width:225px;height:225px;border-radius:50%;background:rgba(38,50,56,.55);border:2px solid rgba(255,255,255,.08);box-shadow:0 0 18px rgba(0,0,0,.35);display:flex;align-items:center;justify-content:center}
.accent-band{left:0;top:713px;width:675px;height:11px;background:var(--red)}
.settings-panel{left:0;top:724px;width:675px;height:476px;background:var(--white)}
.section-head{display:flex;align-items:center;gap:14px;color:var(--teal);font-size:27px;font-weight:500}
.chip{height:45px;padding:0 20px;background:var(--white);box-shadow:0 1px 4px rgba(0,0,0,.25);font-size:25px;color:var(--ink);display:flex;align-items:center;border-radius:2px}
.panel-divider{left:0;top:249px;width:675px;height:2px;background:#e6e8ea}
.unit{font-size:28px}
.toggle-track{left:500px;top:334px;width:66px;height:10px;border-radius:5px;background:var(--ink)}
.toggle-knob{left:528px;top:316px;width:46px;height:46px;border-radius:50%;background:var(--ink)}
.lens{left:-88px;top:223px;width:236px;height:236px;border-radius:50%;background:var(--white);box-shadow:0 3px 14px rgba(0,0,0,.28);overflow:hidden}
.lens-content{left:112px;top:94px;display:flex;align-items:center;gap:14px;color:var(--teal);font-size:40px;font-weight:500;white-space:nowrap}
</style>
</head>
<body>
<div class="abs status-bar">
  <svg width="26" height="22" viewBox="0 0 26 22"><path d="M1 3 Q13 -4 25 3 L13 20Z" fill="#fff"/></svg>
  <svg width="22" height="22" viewBox="0 0 22 22"><path d="M21 1 V21 H1Z" fill="#fff" opacity=".5"/><path d="M21 9 V21 H9Z" fill="#fff"/></svg>
  <svg width="14" height="24" viewBox="0 0 14 24"><rect x="1" y="3" width="12" height="20" fill="#fff"/><rect x="4" y="0" width="6" height="3" fill="#fff"/></svg>
  <span>12:30</span>
</div>

<section class="abs app-screen">
  <div class="abs app-bar">
    <svg class="abs" style="left:40px;top:42px" width="36" height="26" viewBox="0 0 36 26"><rect y="0" width="36" height="4" fill="#fff"/><rect y="11" width="36" height="4" fill="#fff"/><rect y="22" width="36" height="4" fill="#fff"/></svg>
    <div class="abs app-title">Activities</div>
    <div class="abs tab-label">ACTIVITIES</div>
    <div class="abs tab-line"></div>
  </div>
  <article class="abs card" style="top:229px;height:255px">
    <span class="tag" style="top:14px;color:var(--yellow)">#MOVIES</span>
    <span class="title" style="top:36px">We're Going</span>
    <span class="rule" style="top:100px;height:60px"></span>
    <span class="label" style="top:104px">PERSON</span>
    <span class="value" style="top:128px">3</span>
    <span class="divider" style="top:178px"></span>
    <span style="position:absolute;left:28px;top:190px;width:54px;height:54px;border-radius:50%;background:#e4e6e7"></span>
    <span style="position:absolute;left:112px;top:193px;font-size:14px;color:var(--muted);white-space:nowrap">Posted by</span>
    <span style="position:absolute;left:112px;top:214px;font-size:20px;color:var(--ink)">Oren</span>
  </article>
  <article class="abs card" style="top:506px;height:220px">
    <span class="tag" style="top:14px;color:var(--teal)">#RUNNING</span>
    <span class="title" style="top:36px">Running</span>
    <span class="rule" style="top:100px;height:60px"></span>
    <span class="label" style="top:104px">PERSON</span>
    <span class="value" style="top:128px">30</span>
  </article>
</section>

<nav class="abs drawer">
  <div class="abs menu-item" style="top:16px">
    <svg viewBox="0 0 24 24"><path d="M10 20v-6h4v6h5v-8h3L12 3 2 12h3v8z"/></svg>Home</div>
  <div class="abs menu-item" style="top:152px">
    <svg viewBox="0 0 24 24"><path d="M15.5 14h-.8l-.3-.3A6.5 6.5 0 1 0 9.5 16a6.5 6.5 0 0 0 4.2-1.6l.3.3v.8l5 5 1.5-1.5-5-5zm-6 0a4.5 4.5 0 1 1 0-9 4.5 4.5 0 0 1 0 9z"/></svg>Searching Setting</div>
  <div class="abs menu-item" style="top:298px">
    <svg viewBox="0 0 24 24"><path d="M12 6a2 2 0 1 1 0 4 2 2 0 0 1 0-4m0 9c2.7 0 5.8 1.3 6 2v1H6v-1c.2-.7 3.3-2 6-2m0-11a4 4 0 1 0 0 8 4 4 0 0 0 0-8zm0 9c-2.7 0-8 1.3-8 4v3h16v-3c0-2.7-5.3-4-8-4z"/></svg>Profile Setting</div>
  <div class="abs menu-item" style="top:438px;border-bottom:none">
    <svg viewBox="0 0 24 24"><path d="M12 17.3 18.2 21l-1.6-7L22 9.2l-7.2-.6L12 2 9.2 8.6 2 9.2 7.5 14l-1.7 7z"/></svg>Rate Us</div>
  <div class="abs logout-ring">
    <svg width="74" height="74" viewBox="0 0 24 24" fill="none" stroke="#8ba0a8" stroke-width="1.6"><path d="M9 4h11v16H9v-4"/><path d="M9 8V4"/><path d="M3 12h11M10.5 8.5 14 12l-3.5 3.5"/></svg>
  </div>
</nav>

<div class="abs accent-band"></div>

<section class="abs settings-panel">
  <div class="abs section-head" style="left:50px;top:33px">
    <svg width="34" height="34" viewBox="0 0 24 24" fill="none" stroke="var(--teal)" stroke-width="2"><circle cx="12" cy="12" r="10"/><path d="M2 12h20M12 2c3 3 3 17 0 20M12 2c-3 3-3 17 0 20"/></svg>
    Language
  </div>
  <div class="abs chip" style="left:97px;top:99px">Icelandic</div>
  <div class="abs chip" style="left:263px;top:99px">Norwegian</div>
  <div class="abs chip" style="left:441px;top:99px">Spanish</div>
  <div class="abs chip" style="left:97px;top:165px">English</div>
  <div class="abs panel-divider"></div>

  <div class="abs section-head" style="left:97px;top:322px">Distance</div>
  <span class="abs unit" style="left:358px;top:322px;color:var(--muted)">Kilometre</span>
  <div class="abs toggle-track"></div>
  <div class="abs toggle-knob"></div>
  <span class="abs unit" style="left:592px;top:322px;color:var(--ink);font-weight:500">Mile</span>

  <div class="abs lens">
    <div class="abs lens-content">
      <svg width="56" height="56" viewBox="0 0 24 24"><path d="M12 1 23 12 12 23 1 12z" fill="var(--teal)"/><path d="M8 15v-3.5h6V9l3.5 3.2L14 15.5V13H9.5v2z" fill="#fff"/></svg>
      <span>Distance</span>
    </div>
  </div>
</section>
</body>
</html>
```